IT Consulting, IT Guru, Software Development, Network Solutions, Hosting

Attached is logo for our company, we just was the designers to come up with creative ideas to use the logo and the theme to come with creative and energetic business cards that leave an impression and stick in people's head.

Target Market(s)

Medical, Law, Entertainment, Real estate, any small to medium size business.

Industry/Entity Type

Business

Font styles to use
Serif
Sans Serif

```html
<!DOCTYPE html>
<html lang="en">
<head>
<meta charset="utf-8">
<title>Voltrane Business Card</title>
<link rel="stylesheet" href="https://fonts.googleapis.com/css2?family=Questrial&display=swap">
<style>
  :root {
    --page-bg: #ffffff;
    --card-dark: #141516;
    --card-mid: #232527;
    --brand-yellow: #f2c300;
    --text-light: #f1f1f1;
    --text-muted: #c9c9c9;
    --divider: #6b6b6b;
  }
  * { box-sizing: border-box; margin: 0; padding: 0; }
  html, body {
    width: 1200px;
    height: 900px;
    overflow: hidden;
    background: var(--page-bg);
    font-family: "Questrial", "Century Gothic", sans-serif;
  }
  .card-set {
    position: absolute;
    top: 290px;
    left: 40px;
    display: flex;
    gap: 40px;
  }
  .card {
    position: relative;
    width: 540px;
    height: 320px;
    border-radius: 24px;
    background: radial-gradient(ellipse at 50% 40%, var(--card-mid) 0%, var(--card-dark) 75%);
    overflow: hidden;
  }
  .brand-name {
    color: var(--brand-yellow);
    font-size: 58px;
    letter-spacing: 1px;
    line-height: 1;
  }
  .card-front .brand-name {
    position: absolute;
    top: 58px;
    left: 78px;
  }
  .accent-band {
    position: absolute;
    top: 138px;
    left: 0;
    width: 100%;
    height: 8px;
    background: var(--brand-yellow);
  }
  .holder {
    position: absolute;
    top: 178px;
    right: 362px;
    text-align: right;
  }
  .holder-name {
    color: var(--brand-yellow);
    font-size: 17px;
    line-height: 1.2;
  }
  .holder-title {
    color: var(--text-muted);
    font-size: 12px;
  }
  .contact-divider {
    position: absolute;
    top: 176px;
    left: 194px;
    width: 1px;
    height: 108px;
    background: var(--divider);
  }
  .contact-list {
    position: absolute;
    top: 176px;
    left: 206px;
    list-style: none;
    color: var(--text-light);
    font-size: 17px;
    line-height: 23px;
  }
  .contact-list li {
    display: flex;
    align-items: center;
    gap: 7px;
  }
  .contact-list .icon {
    width: 18px;
    height: 18px;
    flex: none;
    fill: var(--brand-yellow);
  }
  .contact-list .no-icon { padding-left: 25px; }
  .card-back {
    display: flex;
    align-items: center;
    justify-content: center;
  }
</style>
</head>
<body>
  <main class="card-set">
    <section class="card card-front">
      <div class="brand-name">VOLTRANE</div>
      <div class="accent-band"></div>
      <div class="holder">
        <p class="holder-name">Dana Mercer</p>
        <p class="holder-title">Manager</p>
      </div>
      <div class="contact-divider"></div>
      <ul class="contact-list">
        <li>
          <svg class="icon" viewBox="0 0 24 24" aria-hidden="true"><path d="M6.6 10.8a15.1 15.1 0 0 0 6.6 6.6l2.2-2.2a1 1 0 0 1 1-.25 11.4 11.4 0 0 0 3.6.57 1 1 0 0 1 1 1V20a1 1 0 0 1-1 1A17 17 0 0 1 3 4a1 1 0 0 1 1-1h3.5a1 1 0 0 1 1 1c0 1.25.2 2.45.57 3.57a1 1 0 0 1-.25 1z"/></svg>
          1800-555-0142
        </li>
        <li>
          <svg class="icon" viewBox="0 0 24 24" aria-hidden="true"><path d="M2 5h20v14H2z M4 7v.5l8 5.5 8-5.5V7z" fill-rule="evenodd"/></svg>
          info@voltrane.com
        </li>
        <li>
          <svg class="icon" viewBox="0 0 24 24" aria-hidden="true"><path d="M12 2a10 10 0 1 0 0 20 10 10 0 0 0 0-20zm-1 2.1V8H7.4A8 8 0 0 1 11 4.1zm2 0A8 8 0 0 1 16.6 8H13zM6.5 10H11v4H6.5a8 8 0 0 1 0-4zm6.5 0h4.5a8 8 0 0 1 0 4H13zm-5.6 6H11v3.9A8 8 0 0 1 7.4 16zm5.6 0h3.6a8 8 0 0 1-3.6 3.9z"/></svg>
          www.voltrane.com
        </li>
        <li>
          <svg class="icon" viewBox="0 0 24 24" aria-hidden="true"><path d="M12 3 2 12h3v8h5v-5h4v5h5v-8h3z"/></svg>
          2715 Harbor Rd. Suite 410
        </li>
        <li class="no-icon">Coral Bay, FL 33021</li>
      </ul>
    </section>

    <section class="card card-back">
      <div class="brand-name">VOLTRANE</div>
    </section>
  </main>
</body>
</html>
```